Personal Training Studio Checkin App (or URL based)

I would like a simple web based app built for our  business. We have a training studio with a simple business model. All our clients buy sessions in packages either 4, 8, or 12 at a time. We want something that a trainer can pull up and Check in a client. This will record the date and time the client was checked in, by what trainer, and what type of session. This system will keep track of the following:
Whenever a Client Checks in so it will ‘tick off’ a session on their package (ie- they have gone from 11 sessions left to 10 sessions left)
Track what sessions a particular trainer does so we can pay them at the end of the week and look at who they trained, what type of session and how many
Look at client activity: Every time they check in, Recharge their package, any activity related to the client, even if it was admin – like deleting a session that was mistakenly recorded.
This will keep a database of clients added and all their activity
The pdf I have included lays out how I think it would work and the features I want
I would like this to run off an tablora that we have at our front check in counter. It can be an app or a URL that use.
***THIS PROJECT IS NOT SO MUCH ABOUT DESIGN BUT ABOUT FUNCTIONALITY OF THE APPLICATION. IT MUST HAVE THE FEATURES I HAVE ASKED FOR THAT WORK TOGETHER. I AM WILLING TO PAY A LITTLE MORE AS A BONUS IF YOU CAN ACCOMPLISH THIS. ALSO IF I FIN THE RIGHT PERSON THAT CAN DO THIS I WILL MAKE IT A GUARNTEED PROJECT.

- Functionality and Track and record all the info we need

```html
<!DOCTYPE html>
<html lang="en">
<head>
<meta charset="utf-8">
<title>Trainer Report – Corestride Training Studio</title>
<link rel="stylesheet" href="https://fonts.googleapis.com/css2?family=Noto+Sans:wght@400;500;600&display=swap">
<style>
  :root {
    --sidebar-bg: #f7f8fa;
    --main-bg: #f4f5f5;
    --text: #212529;
    --nav-text: #4a4d52;
    --icon: #4a4d52;
    --accent: #ea6133;
    --primary: #0d6efd;
    --border: #dee2e6;
    --card-bg: #ffffff;
    --card-head: #f7f7f7;
  }
  * { box-sizing: border-box; margin: 0; padding: 0; }
  html, body { width: 1200px; height: 834px; overflow: hidden; }
  body {
    font-family: "Noto Sans", sans-serif;
    color: var(--text);
    background: var(--main-bg);
    display: flex;
  }
  .sidebar {
    width: 285px;
    height: 834px;
    background: var(--sidebar-bg);
    padding: 0 16px;
    position: relative;
  }
  .brand {
    height: 92px;
    display: flex;
    align-items: center;
    justify-content: center;
    gap: 7px;
    padding-top: 0;
  }
  .brand-mark {
    width: 12px; height: 12px; background: var(--accent); border-radius: 50%;
  }
  .brand-name {
    font-size: 17px; font-weight: 600; color: var(--nav-text); letter-spacing: 0.3px;
  }
  .nav { list-style: none; }
  .nav-item {
    position: absolute;
    left: 16px;
    width: 253px;
    height: 52px;
    display: flex;
    align-items: center;
    padding-left: 24px;
    gap: 13px;
    font-size: 16px;
    color: var(--nav-text);
    border-radius: 5px;
  }
  .nav-item svg { width: 19px; height: 19px; fill: var(--icon); flex: none; }
  .nav-item.active { background: var(--accent); color: #fff; font-weight: 500; }
  .nav-item.active svg { fill: #fff; }
  .divider {
    position: absolute; left: 16px; width: 253px; top: 396px;
    border-top: 1px solid #d5d8dc;
  }
  .main { flex: 1; padding: 0 25px; position: relative; }
  .page-title {
    position: absolute; left: 25px; top: 23px;
    font-size: 28px; font-weight: 500; line-height: 40px;
  }
  .card {
    position: absolute; left: 25px; top: 91px;
    width: 865px; height: 146px;
    background: var(--card-bg);
    border: 1px solid var(--border);
    border-radius: 5px;
    box-shadow: 0 2px 6px rgba(0,0,0,0.08);
    overflow: hidden;
  }
  .card-header {
    height: 42px; background: var(--card-head);
    border-bottom: 1px solid var(--border);
    padding-left: 16px;
    display: flex; align-items: center;
    font-size: 19px; font-weight: 600;
  }
  .report-form { position: relative; height: 104px; }
  .field { position: absolute; top: 20px; }
  .field label { display: block; font-size: 16px; line-height: 22px; margin-bottom: 7px; }
  .control {
    height: 38px; border: 1px solid var(--border); border-radius: 5px;
    background: #fff; display: flex; align-items: center; justify-content: space-between;
    padding: 0 12px; font-size: 16px;
  }
  .control svg { width: 15px; height: 15px; }
  .field-trainer { left: 16px; width: 261px; }
  .field-start { left: 302px; width: 189px; }
  .field-end { left: 516px; width: 190px; }
  .btn-view {
    position: absolute; left: 731px; top: 49px; width: 117px; height: 38px;
    background: var(--primary); color: #fff; border: none; border-radius: 5px;
    font: 16px "Noto Sans", sans-serif;
  }
</style>
</head>
<body>
  <aside class="sidebar">
    <div class="brand">
      <span class="brand-mark"></span>
      <span class="brand-name">Corestride Training Studio</span>
    </div>
    <ul class="nav">
      <li class="nav-item" style="top:97px">
        <svg viewBox="0 0 20 20"><rect x="1" y="1" width="8" height="18"/><rect x="11" y="1" width="8" height="7"/><rect x="11" y="10" width="8" height="9"/></svg>Dashboard</li>
      <li class="nav-item" style="top:153px">
        <svg viewBox="0 0 20 20"><path d="M4 1h12a2 2 0 0 1 2 2v14a2 2 0 0 1-2 2H4a2 2 0 0 1-2-2V3a2 2 0 0 1 2-2zm0 2v14h12V3zm6 3a3 3 0 1 1 0 6 3 3 0 0 1 0-6zm-4 9c0-2 2-3 4-3s4 1 4 3z"/></svg>Trainer Panel</li>
      <li class="nav-item" style="top:210px">
        <svg viewBox="0 0 20 20"><circle cx="6" cy="7" r="3.5"/><path d="M0 17c0-3.5 3-5 6-5s6 1.5 6 5z"/><rect x="13" y="6" width="7" height="1.5"/><rect x="14" y="10" width="6" height="1.5"/><rect x="14" y="14" width="6" height="1.5"/></svg>Client Details</li>
      <li class="nav-item active" style="top:267px">
        <svg viewBox="0 0 20 20"><path d="M4 1h8l5 5v11a2 2 0 0 1-2 2H4a2 2 0 0 1-2-2V3a2 2 0 0 1 2-2zm0 2v14h11V7h-4V3z"/><rect x="6" y="12" width="2" height="4"/><rect x="9" y="10" width="2" height="6"/><rect x="12" y="8" width="2" height="8"/></svg>Trainer Report</li>
      <li class="nav-item" style="top:323px">
        <svg viewBox="0 0 20 20"><path d="M5 0h2v2h6V0h2v2h3a1 1 0 0 1 1 1v15a1 1 0 0 1-1 1H2a1 1 0 0 1-1-1V3a1 1 0 0 1 1-1h3zM3 6v11h14V6z"/><path d="M7 11l2 2 4-4 1 1-5 5-3-3z"/></svg>Session Report</li>
      <li class="nav-item" style="top:413px">
        <svg viewBox="0 0 20 20"><circle cx="7" cy="6" r="4"/><path d="M0 18c0-4 3-6 7-6s7 2 7 6z"/><rect x="16" y="8" width="1.5" height="6"/><rect x="14" y="10.25" width="6" height="1.5"/></svg>Add New Client</li>
      <li class="nav-item" style="top:470px">
        <svg viewBox="0 0 20 20"><path d="M10 1a9 9 0 1 1 0 18 9 9 0 0 1 0-18zm-1 12.5l6-6-1.4-1.4L9 10.7 6.4 8.1 5 9.5z"/></svg>Client Check-in</li>
    </ul>
    <div class="divider"></div>
  </aside>

  <main class="main">
    <h1 class="page-title">Trainer Report</h1>
    <section class="card">
      <div class="card-header">Generate Report</div>
      <form class="report-form">
        <div class="field field-trainer">
          <label>Trainer Name</label>
          <div class="control">John Doe
            <svg viewBox="0 0 16 16"><path d="M2 5l6 6 6-6" fill="none" stroke="#212529" stroke-width="1.8"/></svg>
          </div>
        </div>
        <div class="field field-start">
          <label>Start Date</label>
          <div class="control">dd/mm/yyyy
            <svg viewBox="0 0 16 16"><path d="M1 2h14v13H1z M3 6v7h10V6z" fill="#111" fill-rule="evenodd"/><rect x="4" y="0" width="2" height="3" fill="#111"/><rect x="10" y="0" width="2" height="3" fill="#111"/></svg>
          </div>
        </div>
        <div class="field field-end">
          <label>End Date</label>
          <div class="control">dd/mm/yyyy
            <svg viewBox="0 0 16 16"><path d="M1 2h14v13H1z M3 6v7h10V6z" fill="#111" fill-rule="evenodd"/><rect x="4" y="0" width="2" height="3" fill="#111"/><rect x="10" y="0" width="2" height="3" fill="#111"/></svg>
          </div>
        </div>
        <button type="button" class="btn-view">View</button>
      </form>
    </section>
  </main>
</body>
</html>
```